Business Cards, Stationery, Email signature
and Stationary
Business Cards, Stationery, Email signature - Construction
Creative Brief
Use specific fonts
looking for strong bold lettering
Bright & Fun-filled
Marta Quillen
President
2873 E Marlow Street Orange, CA 94153
marta@larkwoodltdroofing.com
larkwoodltdroofing.com
Was considering having a black business cards so I really wanted to logo to "pop". Even though we are construction I love a card that has personality and fun.

```html
<!DOCTYPE html>
<html lang="en">
<head>
<meta charset="utf-8">
<title>Larkwood Ltd — Business Card</title>
<link href="https://fonts.googleapis.com/css2?family=Cinzel:wght@600&family=Lato:wght@400;700&display=swap" rel="stylesheet">
<style>
  :root {
    --backdrop: #e9e6e1;
    --card-black: #0b0c0e;
    --card-charcoal: #23252a;
    --gold: #e7b35a;
    --gold-light: #f5cf84;
    --blue-deep: #0d4f8c;
    --blue-bright: #35a9e4;
    --silver: #c9ccd1;
    --white: #ffffff;
  }
  * { margin: 0; padding: 0; box-sizing: border-box; }
  html, body { width: 1200px; height: 646px; overflow: hidden; background: var(--backdrop); }
  .canvas {
    width: 1200px; height: 646px;
    display: flex; align-items: center; justify-content: center; gap: 60px;
  }
  .card {
    position: relative; width: 525px; height: 300px; overflow: hidden;
    border-radius: 4px;
    background: radial-gradient(ellipse at 40% 35%, var(--card-charcoal), var(--card-black) 75%);
    box-shadow: 0 10px 24px rgba(0,0,0,.25);
  }
  .brand { display: flex; align-items: center; }
  .brand-dot {
    flex: none; width: 78px; height: 78px; border-radius: 50%;
    background: radial-gradient(circle at 40% 40%, var(--gold-light), var(--gold));
  }
  .brand-rule { flex: none; width: 2px; height: 90px; background: var(--silver); margin: 0 16px; opacity: .8; }
  .brand-name {
    font-family: "Cinzel", serif; font-weight: 600; font-size: 34px;
    color: var(--blue-bright); letter-spacing: 1px; white-space: nowrap;
  }
  .card-front .brand { position: absolute; left: 60px; top: 92px; }
  .front-web {
    position: absolute; left: 172px; top: 190px;
    font-family: "Lato", sans-serif; font-weight: 700; font-size: 13px;
    color: var(--silver); letter-spacing: 1.5px; white-space: nowrap;
  }
  .card-back .waves { position: absolute; inset: 0; }
  .card-back .brand { position: absolute; left: 34px; top: 30px; }
  .card-back .brand-dot { width: 66px; height: 66px; }
  .card-back .brand-rule { height: 76px; margin: 0 14px; }
  .card-back .brand-name { font-size: 30px; }
  .holder { position: absolute; left: 56px; top: 150px; font-family: "Lato", sans-serif; }
  .holder-name { font-size: 17px; font-weight: 700; color: var(--gold); white-space: nowrap; }
  .holder-title { font-size: 13px; color: var(--gold); margin-top: 3px; padding-left: 14px; }
  .contact {
    position: absolute; right: 22px; top: 158px; text-align: right; font-style: normal;
    font-family: "Lato", sans-serif; font-size: 11.5px; line-height: 1.5; color: var(--white);
    white-space: nowrap;
  }
  .contact .gap { height: 5px; }
  .contact .web { font-weight: 700; letter-spacing: 1px; }
</style>
</head>
<body>
<main class="canvas">
  <section class="card card-front">
    <div class="brand">
      <div class="brand-dot"></div>
      <div class="brand-rule"></div>
      <div class="brand-name">Larkwood Ltd</div>
    </div>
    <div class="front-web">www.larkwoodltdroofing.com</div>
  </section>

  <section class="card card-back">
    <svg class="waves" viewBox="0 0 525 300" preserveAspectRatio="none" aria-hidden="true">
      <defs>
        <linearGradient id="blueBand" x1="0" y1="0" x2="1" y2="1">
          <stop offset="0" stop-color="#35a9e4"/>
          <stop offset="1" stop-color="#0d4f8c"/>
        </linearGradient>
      </defs>
      <path d="M0 300 L0 292 C60 280 120 284 175 272 L190 300 Z" fill="#0a3a6a" opacity=".8"/>
      <path d="M0 288 C60 276 120 280 175 268" fill="none" stroke="var(--gold-light)" stroke-width="3"/>
      <path d="M140 300 C200 240 230 160 300 135 C380 110 460 120 525 112 L525 300 Z" fill="url(#blueBand)"/>
      <path d="M130 300 C190 236 220 152 296 126 C376 100 460 110 525 102" fill="none" stroke="var(--gold)" stroke-width="5"/>
    </svg>
    <div class="brand">
      <div class="brand-dot"></div>
      <div class="brand-rule"></div>
      <div class="brand-name">Larkwood Ltd</div>
    </div>
    <div class="holder">
      <div class="holder-name">Marta Quillen</div>
      <div class="holder-title">President</div>
    </div>
    <address class="contact">
      <div>2873 E Marlow Street</div>
      <div>Orange, CA 94153</div>
      <div class="gap"></div>
      <div>(T) 888-555-0147 &nbsp;(F) 714-555-0182</div>
      <div>(C) 714-555-0139</div>
      <div>marta@larkwoodltdroofing.com</div>
      <div class="web">www.larkwoodltdroofing.com</div>
    </address>
  </section>
</main>
</body>
</html>
```